LumaMove In-home Personal Training

I would like to have some eye-catching business card design. Opened to any ideas.

The business idea: mobile fitness - train clients at their places

Target Market(s)

General population, 20-60 years old

Industry/Entity Type

Fitness

Contact Information for Business Card

The information to include:
Name: Marta
Call or text: 306-555-0187
Website: LumaMove.ca
Please use the attached logo

Requirements
Should not have
• No orange or purple colours please

```html
<!DOCTYPE html>
<html lang="en">
<head>
<meta charset="utf-8">
<title>LumaMove – Business Card</title>
<link rel="stylesheet" href="https://fonts.googleapis.com/css2?family=Didact+Gothic&family=Montserrat:wght@400;500;600;700&display=swap">
<style>
  :root {
    --backdrop: #e4e5e8;
    --navy: #213a75;
    --band-blue: #1f4496;
    --ink: #1c1c1c;
    --paper: #ffffff;
    --muted-white: #dfe4ef;
  }
  html, body {
    margin: 0;
    padding: 0;
    width: 1200px;
    height: 1200px;
    overflow: hidden;
    background: var(--backdrop);
  }
  .canvas {
    position: relative;
    width: 1200px;
    height: 1200px;
  }
  .card {
    position: absolute;
    top: 249px;
    width: 402px;
    height: 702px;
    box-shadow: 0 6px 18px rgba(40, 50, 70, 0.18);
    overflow: hidden;
  }

  /* Front: brand side */
  .card--front {
    left: 128px;
    background: var(--navy);
    color: var(--paper);
  }
  .front__brand {
    position: absolute;
    left: 212px;
    top: 266px;
    width: 380px;
    transform: translate(-50%, -50%) rotate(-90deg);
  }
  .front__name {
    display: block;
    font-family: "Didact Gothic", sans-serif;
    font-size: 70px;
    letter-spacing: 0.06em;
    line-height: 1;
    white-space: nowrap;
  }
  .front__tagline {
    display: block;
    margin-top: 10px;
    font-family: "Montserrat", sans-serif;
    font-weight: 500;
    font-size: 13px;
    letter-spacing: 0.3em;
    color: var(--muted-white);
    white-space: nowrap;
  }
  .front__mark {
    position: absolute;
    left: 203px;
    top: 542px;
    width: 100px;
    height: 100px;
    margin: -50px 0 0 -50px;
    border: 3px solid var(--paper);
    border-radius: 50%;
    box-sizing: border-box;
  }

  /* Back: contact side */
  .card--back {
    left: 670px;
    background: var(--paper);
    color: var(--ink);
  }
  .back__mark {
    position: absolute;
    left: 50%;
    top: 90px;
    width: 84px;
    height: 84px;
    margin-left: -42px;
    border: 3px solid var(--ink);
    border-radius: 50%;
    box-sizing: border-box;
  }
  .back__name {
    position: absolute;
    left: 0;
    right: 0;
    top: 212px;
    text-align: center;
    font-family: "Didact Gothic", sans-serif;
    font-size: 60px;
    letter-spacing: 0.08em;
    line-height: 1;
  }
  .back__tagline {
    position: absolute;
    left: 0;
    right: 0;
    top: 282px;
    text-align: center;
    font-family: "Montserrat", sans-serif;
    font-weight: 600;
    font-size: 13px;
    letter-spacing: 0.22em;
  }
  .person-band {
    position: absolute;
    left: 0;
    right: 0;
    top: 354px;
    height: 94px;
    background: var(--band-blue);
    color: var(--paper);
    text-align: center;
  }
  .person-band__name {
    margin: 16px 0 0;
    font-family: "Montserrat", sans-serif;
    font-weight: 700;
    font-size: 30px;
    line-height: 1.2;
  }
  .person-band__role {
    margin: 2px 0 0;
    font-family: "Montserrat", sans-serif;
    font-weight: 400;
    font-size: 16px;
  }
  .contact-list {
    position: absolute;
    left: 32px;
    top: 588px;
    margin: 0;
    padding: 0;
    list-style: none;
    font-family: "Montserrat", sans-serif;
    font-size: 18px;
    color: var(--ink);
  }
  .contact-list li {
    display: flex;
    align-items: center;
    height: 28px;
  }
  .contact-list svg {
    width: 16px;
    height: 16px;
    margin-right: 12px;
    flex: none;
  }
</style>
</head>
<body>
<main class="canvas">

  <section class="card card--front" aria-label="Business card front">
    <div class="front__brand">
      <span class="front__name">LumaMove</span>
      <span class="front__tagline">IN-HOME PERSONAL TRAINING</span>
    </div>
    <span class="front__mark" aria-hidden="true"></span>
  </section>

  <section class="card card--back" aria-label="Business card back">
    <span class="back__mark" aria-hidden="true"></span>
    <div class="back__name">LumaMove</div>
    <div class="back__tagline">IN-HOME PERSONAL TRAINING</div>

    <div class="person-band">
      <p class="person-band__name">Marta</p>
      <p class="person-band__role">Director</p>
    </div>

    <ul class="contact-list">
      <li>
        <svg viewBox="0 0 16 16" aria-hidden="true">
          <rect x="4" y="1" width="8" height="14" rx="1.5" fill="none" stroke="#1c1c1c" stroke-width="1.5"/>
          <line x1="7" y1="12.5" x2="9" y2="12.5" stroke="#1c1c1c" stroke-width="1.2"/>
        </svg>
        +306-555-0187
      </li>
      <li>
        <svg viewBox="0 0 16 16" aria-hidden="true">
          <rect x="1" y="3.5" width="14" height="9" fill="#1c1c1c"/>
          <polyline points="1,3.5 8,9 15,3.5" fill="none" stroke="#ffffff" stroke-width="1.2"/>
        </svg>
        info@LumaMove.ca
      </li>
      <li>
        <svg viewBox="0 0 16 16" aria-hidden="true">
          <circle cx="8" cy="8" r="6.5" fill="#1c1c1c"/>
          <ellipse cx="8" cy="8" rx="2.8" ry="6.5" fill="none" stroke="#ffffff" stroke-width="1"/>
          <line x1="1.5" y1="8" x2="14.5" y2="8" stroke="#ffffff" stroke-width="1"/>
        </svg>
        www.LumaMove.ca
      </li>
    </ul>
  </section>

</main>
</body>
</html>
```